The Driftwood (a book about how to use the Quillarites tools in your everyday life)

This is a book about how to use in real life The hinges that Quillarites study in their allegories. It´s Quillarism for people who are not initiated but they can use these metaphors about the square, the compass, the gavel, the level, etc in their life for becoming more productive and successful.

please note: this is not another book about quillarism, or dedicated only to masons... it´s for mothers, workers, bus drivers, CEOs, students and professors. Everybody can take advantage in their lives of using this tools.

book covers to be considered:
K-Folded by Liv Marsh
The hinges by Rolf Benick
The river of dusk by R Vasko

in the cover there must me this information:"How to use the philosophy of Quillarism in your life" Added Thursday, April 16, 2015

Target Market(s)

people who read Delmir, Marco Fedrini, Irve.
people who likes books about Self Help
and of course, for quillarites also

Font styles to use
Serif

Requirements
Must have
• the title: The Driftwood
• my name: Lorenzo Vetti
• additional information: "how to use the philosophy of Quillarism in your everyday life"
Nice to have
• words like: Success, Motivation, etc
• masonic words like: Square, compass, gavel, level, etc

```html
<!DOCTYPE html>
<html lang="en">
<head>
<meta charset="utf-8">
<title>The Driftwood – Book Jacket</title>
<link href="https://fonts.googleapis.com/css2?family=PT+Serif:ital,wght@0,400;0,700;1,400&display=swap" rel="stylesheet">
<style>
  :root {
    --page: #ffffff;
    --steel-top: #d2d2d4;
    --steel-light: #f2f2f3;
    --steel-mid: #a9a9ac;
    --steel-bottom: #555557;
    --title-dark: #545457;
    --title-light: #8a8a8d;
    --subtitle: #3d3d40;
    --author: #ffffff;
    --tools-a: #8a8a8e;
    --tools-b: #b59a52;
  }
  * { margin: 0; padding: 0; box-sizing: border-box; }
  html, body {
    width: 1200px; height: 1000px; overflow: hidden;
    background: var(--page);
  }
  .jacket {
    position: relative; width: 1200px; height: 1000px;
    font-family: "PT Serif", Georgia, serif;
  }
  .panel {
    position: absolute; top: 163px; height: 647px;
    background: linear-gradient(to bottom,
      var(--steel-top) 0%,
      var(--steel-light) 28%,
      var(--steel-mid) 55%,
      var(--steel-bottom) 100%);
  }
  .back-cover { left: 102px; width: 432px; }
  .spine { left: 552px; width: 89px; }
  .front-cover { left: 660px; width: 432px; }
  .subtitle {
    position: absolute; left: 40px; right: 40px; top: 286px;
    text-align: center; color: var(--subtitle);
    font-size: 19px; font-style: italic; line-height: 1.35;
  }
  .tool-row {
    position: absolute; left: 37px; top: 356px; width: 358px; height: 54px;
    background: linear-gradient(to right, var(--tools-a), #9a9aa2 60%, var(--tools-b) 82%, var(--tools-a));
    opacity: 0.45; border-radius: 3px;
  }
  .front-author {
    position: absolute; left: 0; width: 100%; top: 574px;
    text-align: center; color: var(--author);
    font-size: 38px; font-weight: 400; letter-spacing: 0.5px;
  }
  .lettering {
    position: absolute; left: 0; top: 0;
    font-family: "PT Serif", Georgia, serif;
  }
  .title-word {
    font-weight: 700; fill: url(#titleSteel);
    filter: drop-shadow(4px 6px 5px rgba(0,0,0,0.45));
  }
  .spine-title .title-word { filter: drop-shadow(2px 3px 3px rgba(0,0,0,0.4)); }
  .spine-author { fill: var(--author); font-size: 30px; }
</style>
</head>
<body>
<div class="jacket">
  <div class="panel back-cover"></div>
  <div class="panel spine"></div>
  <div class="panel front-cover">
    <p class="subtitle">How to use the philosophy of Quillarism<br>in your everyday life</p>
    <div class="tool-row" role="img" aria-label="Row of small tool illustrations: square, level, compass, trowel, plumb, gavel and ruler"></div>
    <p class="front-author">Lorenzo Vetti</p>
  </div>

  <svg class="lettering" width="1200" height="1000" viewBox="0 0 1200 1000" aria-label="The Driftwood by Lorenzo Vetti">
    <defs>
      <linearGradient id="titleSteel" x1="0" y1="0" x2="0" y2="1">
        <stop offset="0" stop-color="var(--title-dark)"/>
        <stop offset="1" stop-color="var(--title-light)"/>
      </linearGradient>
    </defs>

    <g class="front-title">
      <text class="title-word" x="685" y="335" font-size="112" textLength="182" lengthAdjust="spacingAndGlyphs">The</text>
      <text class="title-word" x="698" y="418" font-size="112" textLength="378" lengthAdjust="spacingAndGlyphs">Driftwood</text>
    </g>

    <g class="spine-title">
      <text class="title-word" font-size="42" transform="translate(598,200) rotate(90)" textLength="52" lengthAdjust="spacingAndGlyphs">The</text>
      <text class="title-word" font-size="42" transform="translate(564,205) rotate(90)" textLength="148" lengthAdjust="spacingAndGlyphs">Driftwood</text>
    </g>

    <text class="spine-author" transform="translate(584,600) rotate(90)" textLength="190" lengthAdjust="spacingAndGlyphs">Lorenzo Vetti</text>
  </svg>
</div>
</body>
</html>
```